Business card design for IT consulting company

Looking for a simple, modern, clean business card design.
Open to reworking our existing logo.

Attached is our current business cards which we do not like.
Ideally double sided with something simple on the back.
Rectangle / Horizonal only.
No rounded edges on the card.
White as the dominate color is preferred.

Target Market(s)

clients, legal, oil & gas, medical, professionals

Industry/Entity Type

IT, tech, consulting

Contact Information for Business Card

Name, Title, email, phone, cell, website

Font styles to use
Sans Serif

Requirements
Must have
• Clean design
Should not have
• loud colors or unusual fonts, etc

```html
<!DOCTYPE html>
<html lang="en">
<head>
<meta charset="utf-8">
<title>Norvale Solutions – Business Card</title>
<link rel="stylesheet" href="https://fonts.googleapis.com/css2?family=Arimo:wght@400;700&display=swap">
<style>
  :root {
    --backdrop: #3a3a3a;
    --card: #f7f7f7;
    --ink: #1a1a1a;
    --ink-soft: #444444;
    --divider: #c9c9c9;
    --yellow: #f4bf2c;
    --red: #e43d52;
    --blue: #40a9df;
    --navy: #262a6d;
  }
  * { box-sizing: border-box; margin: 0; padding: 0; }
  html, body {
    width: 1200px;
    height: 689px;
    overflow: hidden;
    background: var(--backdrop);
    font-family: "Arimo", Arial, sans-serif;
    color: var(--ink);
  }
  .canvas {
    width: 1200px;
    height: 689px;
    display: flex;
    align-items: center;
    justify-content: center;
    gap: 40px;
  }
  .card {
    width: 540px;
    height: 309px;
    background: var(--card);
    position: relative;
  }

  /* Front */
  .card-front {
    display: flex;
    align-items: center;
    justify-content: center;
  }
  .brand {
    display: flex;
    align-items: center;
    gap: 12px;
    font-weight: 700;
    color: var(--ink);
  }
  .brand-square {
    background: var(--navy);
    border-radius: 6px;
  }
  .card-front .brand { font-size: 34px; }
  .card-front .brand-square { width: 40px; height: 40px; }

  /* Back */
  .card-back {
    display: flex;
    align-items: center;
    padding: 0 36px 0 40px;
  }
  .card-back .brand { font-size: 27px; gap: 10px; width: 262px; }
  .card-back .brand-square { width: 34px; height: 34px; border-radius: 5px; }
  .divider {
    width: 1px;
    height: 130px;
    background: var(--divider);
    margin: 0 26px 0 10px;
  }
  .contact { display: flex; flex-direction: column; }
  .contact-name { font-size: 19px; font-weight: 700; line-height: 1.1; }
  .contact-title { font-size: 12px; color: var(--ink-soft); margin-bottom: 12px; }
  .contact-list { list-style: none; display: flex; flex-direction: column; gap: 4px; }
  .contact-item {
    display: flex;
    align-items: center;
    gap: 8px;
    font-size: 12.5px;
    color: var(--ink);
  }
  .contact-icon {
    width: 14px;
    height: 14px;
    border-radius: 3px;
    display: block;
    flex: none;
  }
  .icon-phone { background: var(--yellow); }
  .icon-mobile { background: var(--red); }
  .icon-email { background: var(--blue); }
  .icon-web { background: var(--navy); }
</style>
</head>
<body>
<main class="canvas">
  <section class="card card-front" aria-label="Card front">
    <div class="brand">
      <span class="brand-square"></span>
      <span class="brand-name">Norvale</span>
    </div>
  </section>

  <section class="card card-back" aria-label="Card back">
    <div class="brand">
      <span class="brand-square"></span>
      <span class="brand-name">Norvale Solutions</span>
    </div>
    <div class="divider"></div>
    <div class="contact">
      <p class="contact-name">Daniel Moss</p>
      <p class="contact-title">IT Consultant</p>
      <ul class="contact-list">
        <li class="contact-item">
          <svg class="contact-icon icon-phone" viewBox="0 0 14 14" aria-hidden="true"><path d="M4 3.5c.6 0 1 1.4 1 1.8s-.7.6-.5 1.1c.4.9 1.2 1.7 2.1 2.1.5.2.7-.5 1.1-.5s1.8.4 1.8 1-.8 1.5-1.6 1.5C5.6 10.5 3.5 8.4 3.5 5.1c0-.8.9-1.6.5-1.6z" fill="#fff"/></svg>
          (888)555-0142
        </li>
        <li class="contact-item">
          <svg class="contact-icon icon-mobile" viewBox="0 0 14 14" aria-hidden="true"><rect x="4.5" y="2.5" width="5" height="9" rx="1" fill="none" stroke="#fff" stroke-width="1.1"/></svg>
          (604) 555-0187
        </li>
        <li class="contact-item">
          <svg class="contact-icon icon-email" viewBox="0 0 14 14" aria-hidden="true"><rect x="3" y="4" width="8" height="6" fill="none" stroke="#fff" stroke-width="1"/><path d="M3 4l4 3.2L11 4" fill="none" stroke="#fff" stroke-width="1"/></svg>
          daniel.moss@norvale.ca
        </li>
        <li class="contact-item">
          <svg class="contact-icon icon-web" viewBox="0 0 14 14" aria-hidden="true"><circle cx="7" cy="7" r="3.6" fill="none" stroke="#fff" stroke-width="1"/><path d="M3.4 7h7.2M7 3.4c1.6 2 1.6 5.2 0 7.2M7 3.4c-1.6 2-1.6 5.2 0 7.2" fill="none" stroke="#fff" stroke-width=".8"/></svg>
          www.norvale.ca
        </li>
      </ul>
    </div>
  </section>
</main>
</body>
</html>
```